Modern & Fresh Halvonix Book Cover

Need a creative e-book cover for my book.

Title: Get Halvonix Clear
Subtitle: Learn How To Easily Choose & Enroll in the Perfect Coverage at the Perfect Time.

Target Market(s)

60-70 year olds in the United States

Font styles to use
Sans Serif

Colors
9bcb3c
33a6d7

Requirements
Must have
• Must look modern and fresh.
• Use our company colors www.TarvoLume.com

```html
<!DOCTYPE html>
<html lang="en">
<head>
<meta charset="utf-8">
<title>Get Halvonix Clear – Cover Concepts</title>
<link rel="stylesheet" href="https://fonts.googleapis.com/css2?family=Bebas+Neue&family=Open+Sans:wght@400;600&display=swap">
<style>
  :root {
    --stage: #e6e6e6;
    --paper: #ffffff;
    --navy: #0b1c6b;
    --navy-light: #3f77c4;
    --green: #8cc63f;
    --red: #d9262c;
    --ink: #2b2b2b;
    --sub-ink: #3a3a3a;
    --band: #ececec;
    --sky: #cfe0ef;
    --sea: #3f78b8;
    --sea-deep: #214f96;
  }
  * { box-sizing: border-box; margin: 0; padding: 0; }
  html, body { width: 1003px; height: 1200px; overflow: hidden; background: var(--stage); }
  .board {
    display: grid;
    grid-template-columns: 501px 502px;
    grid-template-rows: 600px 600px;
    width: 1003px; height: 1200px;
  }
  .cell { position: relative; display: flex; align-items: center; justify-content: center; }
  .cell:nth-child(odd) { border-right: 1px solid #d2d2d2; }
  .cell:nth-child(-n+2) { border-bottom: 1px solid #d2d2d2; }

  .cover {
    position: relative;
    width: 260px; height: 450px;
    background: var(--paper);
    overflow: hidden;
    box-shadow: 0 6px 18px rgba(0,0,0,.18);
  }
  .title {
    position: absolute; top: 22px; left: 0; right: 0;
    text-align: center;
    font-family: "Bebas Neue", sans-serif;
    line-height: .86;
    z-index: 2;
  }
  .title span { display: block; }
  .title .t-get { font-size: 62px; }
  .title .t-brand { font-size: 64px; letter-spacing: -.5px; }
  .title .t-clear { font-size: 118px; letter-spacing: -1px; }

  .grad-navy {
    background: linear-gradient(180deg, var(--navy) 35%, var(--navy-light) 100%);
    -webkit-background-clip: text; background-clip: text; color: transparent;
  }
  .c-green { color: var(--green); }
  .c-red { color: var(--red); }
  .c-ink { color: var(--ink); }

  .subtitle {
    position: absolute; top: 262px; left: 16px; right: 16px;
    padding: 6px 4px;
    text-align: center;
    font-family: "Open Sans", sans-serif;
    font-size: 8.6px; line-height: 1.35;
    color: var(--sub-ink);
    text-transform: uppercase;
    background: linear-gradient(90deg, rgba(236,236,236,0) 0%, var(--band) 20%, var(--band) 80%, rgba(236,236,236,0) 100%);
    z-index: 2;
  }
  .subtitle.on-sky { color: var(--navy); background: linear-gradient(90deg, rgba(255,255,255,0), rgba(255,255,255,.35) 20%, rgba(255,255,255,.35) 80%, rgba(255,255,255,0)); }

  .art { position: absolute; left: 0; right: 0; }

  /* cover 1 */
  .cover--beach .sky-wash {
    position: absolute; left: 0; right: 0; top: 170px; height: 130px;
    background: linear-gradient(180deg, #ffffff 0%, var(--sky) 100%);
  }
  .cover--beach .art { top: 300px; bottom: 0; background: linear-gradient(180deg, #7fa6cc 0%, #5a8fc2 40%, #c9c3b6 100%); }

  /* cover 2 */
  .cover--umbrella .art {
    top: 320px; height: 110px; left: 55px; right: 40px;
    background: radial-gradient(ellipse at 55% 40%, #e23a3e 0%, #c9262b 55%, rgba(255,255,255,0) 72%);
  }

  /* cover 3 */
  .cover--map .art {
    top: 310px; bottom: 14px; left: 18px; right: 18px;
    background: linear-gradient(180deg, #f7f7f7, #f1f1f1);
    border-radius: 4px;
  }

  /* cover 4 */
  .cover--boat .art.sky { top: 300px; height: 96px; background: linear-gradient(180deg, #f4f7fa 0%, #dbe7f1 100%); }
  .cover--boat .art.boat {
    top: 318px; height: 80px; left: 70px; right: 70px;
    background: radial-gradient(ellipse at 45% 45%, #f0a32a 0%, #d98a1c 40%, rgba(230,230,230,.9) 70%, rgba(255,255,255,0) 80%);
  }
  .cover--boat .sea {
    position: absolute; left: 0; right: 0; top: 396px; bottom: 0;
    background: linear-gradient(180deg, var(--sea) 0%, var(--sea-deep) 100%);
  }
  .author {
    position: absolute; left: 0; right: 0; bottom: 18px;
    text-align: center;
    font-family: "Open Sans", sans-serif; font-weight: 600;
    font-size: 13px; letter-spacing: .5px;
    color: #ffffff;
  }
</style>
</head>
<body>
<main class="board">

  <section class="cell">
    <article class="cover cover--beach">
      <div class="sky-wash"></div>
      <h1 class="title">
        <span class="t-get grad-navy">Get</span>
        <span class="t-brand c-green">Halvonix</span>
        <span class="t-clear grad-navy">Clear</span>
      </h1>
      <p class="subtitle on-sky">Learn how to easily choose &amp; enroll in the<br>perfect coverage at the perfect time.</p>
      <div class="art" role="img" aria-label="Photo of a smiling older couple walking bicycles along a sunny beach by the sea"></div>
    </article>
  </section>

  <section class="cell">
    <article class="cover cover--umbrella">
      <h1 class="title">
        <span class="t-get c-ink">Get</span>
        <span class="t-brand c-red">Halvonix</span>
        <span class="t-clear c-ink">Clear</span>
      </h1>
      <p class="subtitle">Learn how to easily choose &amp; enroll in the<br>perfect coverage at the perfect time.</p>
      <div class="art" role="img" aria-label="Illustration of a red umbrella sheltering a white paper family of four"></div>
    </article>
  </section>

  <section class="cell">
    <article class="cover cover--map">
      <h1 class="title">
        <span class="t-get c-ink">Get</span>
        <span class="t-brand c-green">Halvonix</span>
        <span class="t-clear c-ink">Clear</span>
      </h1>
      <p class="subtitle">Learn how to easily choose &amp; enroll in the<br>perfect coverage at the perfect time.</p>
      <div class="art" role="img" aria-label="Hand-drawn mind map with Halvonix at the centre linked to care, costs, doctors, plans and enrollment bubbles"></div>
    </article>
  </section>

  <section class="cell">
    <article class="cover cover--boat">
      <h1 class="title">
        <span class="t-get grad-navy">Get</span>
        <span class="t-brand c-green">Halvonix</span>
        <span class="t-clear grad-navy">Clear</span>
      </h1>
      <p class="subtitle">Learn how to easily choose &amp; enroll in the<br>perfect coverage at the perfect time.</p>
      <div class="art sky"></div>
      <div class="sea"></div>
      <div class="art boat" role="img" aria-label="Illustration of a pill bottle riding in a paper boat folded from a prescription, floating on water"></div>
      <p class="author">AUTHOR'S NAME</p>
    </article>
  </section>

</main>
</body>
</html>
```